Patient Report Folder for modern Chiropractic Clinic

We are looking for someone to design a patient folder and 3 simple info sheets to go along with it.

The design should be clean and masculine with an artsy touch. I am a fan of the Fra Mollego style drawings so would like the background to be a style of parchment paper. The info sheets should follow a similar style.

Please check the “Design Outline” pdf and the “Folder Design” file before getting started. The 3 info sheets are going to be placed in the pocket where “Attachment #3” will be.

- The format should be DIN A4 according to the printing details attached in the files section. Please see the ''Folder Design.jpg'' for the design of the folder.
- All the designs should be different and unique in nature but match each other.
- The text for Info Sheet #3 can be left blank.

It is probably best to take a look at the ''Design Outline'' file first to see how I envision the design to be. Please do not hesitate to ask me questions or to discuss ideas.

Target Market(s)

upper class audience with a focus on health and well-being

Industry/Entity Type

Chiropractic // Health

Requirements
Must have
• The colours should be fitting with the main colours in the logo: #1ccad5 and #b1b2b4
Nice to have
• Fra Mollego Style design and the background on parchment paper style. It is not a must but if anyone can come up with a suitable design and colorway that would be great.

```html
<!DOCTYPE html>
<html lang="en">
<head>
<meta charset="utf-8">
<title>Patient Folder – Inside Spread</title>
<link href="https://fonts.googleapis.com/css2?family=Montserrat:wght@400;500;600&family=Bebas+Neue&family=Mrs+Saint+Delafield&display=swap" rel="stylesheet">
<style>
  :root{
    --backdrop:#bdbcbe;
    --paper:#f3f3f2;
    --paper-shade:#e6e6e5;
    --ink:#2f2f2f;
    --ink-soft:#555;
    --teal:#1ccad5;
    --sage:#cfdcd8;
    --ring:#8fb5ae;
    --stone:#8b8b8b;
    --cream:#f6efe9;
    --pill:#eadbd0;
    --pill-ink:#6d5b52;
    --mocha:#a99890;
    --sand:#e3cdb8;
    --ochre:#efb44a;
  }
  *{box-sizing:border-box;margin:0;padding:0}
  html,body{width:1200px;height:847px;overflow:hidden;background:var(--backdrop)}
  .spread{position:absolute;left:34px;top:24px;width:1132px;height:800px;display:flex;box-shadow:0 10px 30px rgba(0,0,0,.18)}
  .page{position:relative;width:566px;height:800px;background:var(--paper);overflow:hidden;font-family:"Montserrat",sans-serif;color:var(--ink)}
  .page--left{background:linear-gradient(90deg,var(--paper) 80%,var(--paper-shade))}
  .page--right{background:linear-gradient(90deg,var(--paper-shade),var(--paper) 12%)}

  /* Left page */
  .visit-title{position:absolute;top:70px;width:100%;text-align:center;color:var(--teal);font-weight:600;font-size:20px;letter-spacing:.5px}
  .visit-list{position:absolute;top:150px;left:0;width:100%;list-style:none;text-align:center;font-size:12.5px;line-height:1.35}
  .visit-step{margin-bottom:26px}
  .visit-step .dash{display:block;width:14px;height:1px;background:var(--ink);margin:4px auto 3px}
  .visit-step.heading{font-size:13px;letter-spacing:.5px}
  .smile{position:absolute;top:710px;width:100%;text-align:center;color:var(--teal);font-size:22px}

  /* Right page */
  .stress-band{position:absolute;left:150px;top:88px;width:280px;height:36px;background:var(--sage)}
  .stress-title{position:absolute;top:48px;width:100%;text-align:center;font-size:62px;font-weight:400;letter-spacing:4px;color:var(--ink)}
  .stress-script{position:absolute;top:108px;width:100%;text-align:center;font-family:"Mrs Saint Delafield",cursive;font-size:82px;color:var(--ink)}
  .hand-art{position:absolute;left:190px;top:150px;width:220px;height:280px;background:linear-gradient(180deg,rgba(120,120,120,.08),rgba(120,120,120,.18));border-radius:90px 90px 20px 20px}
  .intro{position:absolute;top:212px;left:60px;width:446px;text-align:center;font-size:8.6px;line-height:1.45;color:var(--ink-soft)}
  .emotional{position:absolute;left:165px;top:262px;width:250px;height:250px;border-radius:50%;background:var(--stone);box-shadow:0 0 0 3px var(--paper),0 0 0 5px var(--ring);text-align:center;color:#3a3a3a}
  .emotional h3{margin-top:30px;font-weight:400;font-size:15px;letter-spacing:1.5px}
  .emotional p{margin:12px auto 0;width:190px;font-size:9.5px;line-height:1.5}

  .pocket{position:absolute;left:0;top:340px;width:566px;height:460px;background:var(--cream);clip-path:polygon(0 28%,100% 0,100% 100%,0 100%);box-shadow:0 -4px 10px rgba(0,0,0,.15)}
  .palm-art{position:absolute;right:20px;top:40px;width:220px;height:160px;background:radial-gradient(ellipse at 60% 40%,rgba(227,205,184,.9),rgba(227,205,184,0) 70%)}
  .leaf-art{position:absolute;right:0;top:250px;width:90px;height:120px;background:var(--ochre);border-radius:70px 0 0 50px}
  .leaf-art--low{left:30px;right:auto;top:420px;width:70px;height:40px;border-radius:40px 40px 0 0}
  .sprig-art{position:absolute;left:20px;top:300px;width:70px;height:110px;background:linear-gradient(180deg,rgba(200,200,200,.0),rgba(200,200,200,.35));border-radius:40px}

  .brand-dot{position:absolute;left:224px;top:200px;width:120px;height:120px;border-radius:50%;background:var(--mocha)}
  .brand-name{position:absolute;left:184px;top:332px;width:200px;text-align:center;font-family:"Montserrat",sans-serif;font-weight:500;font-size:14px;letter-spacing:1px;color:var(--pill-ink)}

  .habit{position:absolute;display:flex;align-items:center;height:38px;background:var(--pill);border-radius:6px;font-family:"Bebas Neue",sans-serif;font-size:19px;color:var(--pill-ink);letter-spacing:.3px;line-height:.9}
  .habit--left{padding-left:12px;padding-right:48px}
  .habit--right{padding-left:50px;padding-right:14px}
  .habit--stacked{font-size:15px}
  .habit .icon{position:absolute;top:-6px;width:50px;height:50px;border-radius:50%;background:var(--pill);box-shadow:inset 0 0 0 4px var(--cream);display:flex;align-items:center;justify-content:center}
  .habit--left .icon{right:-10px}
  .habit--right .icon{left:-10px}
  .habit .icon svg{width:26px;height:26px;fill:none;stroke:var(--pill-ink);stroke-width:1.6;stroke-linecap:round;stroke-linejoin:round}
</style>
</head>
<body>
<main class="spread">
  <section class="page page--left">
    <h2 class="visit-title">YOUR NEXT VISIT</h2>
    <ul class="visit-list">
      <li class="visit-step">Make yourself at home<span class="dash"></span>Take of your shoes and jacket</li>
      <li class="visit-step">Let us know you’re here<span class="dash"></span>Check in at the front desk</li>
      <li class="visit-step">Get comfy<span class="dash"></span>Take a seat in the waiting area or the designated adjusting room</li>
      <li class="visit-step">Be excited and be ready<span class="dash"></span>Take of your belt, empty your pockets and take a seat on “The Chair”</li>
      <li class="visit-step heading">ADJUSTING TIME</li>
      <li class="visit-step">Time to say goodbye<span class="dash"></span>Our front desk will help you with EVERYTHING else you need</li>
      <li class="visit-step">Be a better version of yourself<span class="dash"></span>Take a 10 minute walk</li>
    </ul>
    <p class="smile">:)</p>
  </section>

  <section class="page page--right">
    <div class="stress-band"></div>
    <h1 class="stress-title">STRESS</h1>
    <div class="hand-art" role="img" aria-label="Line drawing of an open hand and flower"></div>
    <p class="stress-script">builders</p>
    <p class="intro">Try your best to remove or reduce these stressors from your life as possible. By reducing stress on your body, you increase your parasympathetic nervous system’s influence, which will enable your body’s innate healing to flourish. This in turn will boost your healing and you will reduce injury and sickness.</p>
    <div class="emotional">
      <h3>EMOTIONAL</h3>
      <p>your body being in a constant state of fight or flight, rather than in a relaxed, parasympathetic state.</p>
    </div>

    <div class="pocket">
      <div class="palm-art" role="img" aria-label="Soft beige palm leaves"></div>
      <div class="leaf-art" role="img" aria-label="Ochre tropical leaf"></div>
      <div class="leaf-art leaf-art--low" role="img" aria-label="Ochre tropical leaf"></div>
      <div class="sprig-art" role="img" aria-label="Faint line-drawn sprig"></div>

      <div class="brand-dot"></div>
      <p class="brand-name">Steady Path</p>

      <div class="habit habit--left" style="left:40px;top:225px">SLEEP
        <span class="icon"><svg viewBox="0 0 24 24"><path d="M15 4a8 8 0 1 0 5 12 7 7 0 0 1-5-12z"/><path d="M6 6h.01M9 4h.01"/></svg></span></div>
      <div class="habit habit--left" style="left:40px;top:290px">GET OUTSIDE
        <span class="icon"><svg viewBox="0 0 24 24"><circle cx="16" cy="8" r="4"/><path d="M16 12v8M3 16h10M4 16v4M12 16v4M3 13h10"/></svg></span></div>
      <div class="habit habit--left" style="left:60px;top:370px">MEDITATION
        <span class="icon"><svg viewBox="0 0 24 24"><path d="M12 4v12M8 20l4-4 4 4M12 8l-4 8M12 8l4 8"/></svg></span></div>

      <div class="habit habit--right" style="left:400px;top:150px">READ
        <span class="icon"><svg viewBox="0 0 24 24"><path d="M3 6h7a2 2 0 0 1 2 2v11a2 2 0 0 0-2-2H3zM21 6h-7a2 2 0 0 0-2 2v11a2 2 0 0 1 2-2h7z"/></svg></span></div>
      <div class="habit habit--right habit--stacked" style="left:420px;top:215px">THINK<br>POSITIVE
        <span class="icon"><svg viewBox="0 0 24 24"><path d="M8 20v-4a6 6 0 1 1 9-2l1 3h-3v3"/><path d="M12 8v4M10 10h4"/></svg></span></div>
      <div class="habit habit--right" style="left:430px;top:285px">EXERCISE
        <span class="icon"><svg viewBox="0 0 24 24"><path d="M7 12h10M5 8v8M8 7v10M16 7v10M19 8v8"/></svg></span></div>
    </div>
  </section>
</main>
</body>
</html>
```